Lodgevo and Small Event Venue Site

Looking for a basic site that would also include a seperate landing page for our email list. We have rehabbed an old 1905 Bank Building into a Lodgevo /Small Event Venue (baby showers, birthday parties, mixers, etc) . We are looking for an very nice professional page along with integration with the Lodgevo Booking Calendar. We have a nice logo we can provide you with......The Name Of Our Venue is "The Ivy Lantern Hall".

```html
<!DOCTYPE html>
<html lang="en">
<head>
<meta charset="utf-8">
<title>The Ivy Lantern Hall</title>
<link href="https://fonts.googleapis.com/css2?family=Poppins:wght@300;400;500;600;700&family=Oswald:wght@600;700&display=swap" rel="stylesheet">
<style>
:root{
  --ink:#1b1b1b;
  --dark:#222222;
  --white:#ffffff;
  --muted:#8a8a8a;
  --line:#d8d8d8;
  --rose:#b58c80;
  --brick:#6a3b2c;
}
*{box-sizing:border-box;margin:0;padding:0}
html,body{width:1200px;height:5133px;overflow:hidden}
body{position:relative;background:var(--white);font-family:"Poppins",sans-serif;color:var(--ink)}
.abs{position:absolute}
.center{text-align:center}

/* top bar */
.topbar{left:0;top:0;width:1200px;height:60px;background:var(--ink);color:var(--white);font-size:14px}
.topbar .item{position:absolute;top:20px;display:flex;align-items:center;gap:8px}
.topbar .sep{position:absolute;left:870px;top:10px;width:1px;height:40px;background:#777}
.logo-bump{left:68px;top:34px;width:104px;height:104px;border-radius:50%;background:var(--white)}
.header{left:0;top:60px;width:1200px;height:120px;background:var(--white)}
.brand{left:88px;top:78px;display:flex;align-items:center;gap:10px;font-weight:600;font-size:26px;letter-spacing:1px;color:var(--ink)}
.brand .dot{width:46px;height:46px;border-radius:50%;background:var(--ink)}
.nav{left:612px;top:110px;display:flex;gap:31px;font-size:13.5px;color:#333}

/* hero */
.hero{left:0;top:180px;width:1200px;height:780px;background:linear-gradient(160deg,#2b2320 0%,#4b382e 45%,#5a3a2b 70%,#2f2520 100%)}
.hero h1{position:absolute;left:76px;top:240px;font-family:"Oswald",sans-serif;font-weight:700;font-size:86px;line-height:106px;color:var(--white);letter-spacing:1px}
.hero .cta{position:absolute;left:148px;top:540px;font-size:20px;color:var(--white)}
.hero-arch{left:596px;top:300px;width:508px;height:592px;border-radius:254px 254px 0 0;background:linear-gradient(180deg,#d9d2cb,#b8a99a 60%,#8c7a68)}

/* booking */
.booking{left:46px;top:890px;width:1104px;height:348px;background:var(--white);box-shadow:0 6px 24px rgba(0,0,0,.14)}
.h2{font-size:34px;font-weight:400;letter-spacing:.5px;color:var(--ink)}
.h2 b{font-weight:600}
.field{position:absolute;top:166px;height:70px;border:1.5px solid #9bb0b6;font-size:16px;color:#333;display:flex;align-items:center;padding:0 16px;justify-content:space-between}
.btn-dark{background:var(--ink);color:var(--white);display:flex;align-items:center;justify-content:center;font-size:16px}

/* events */
.event-card{top:1466px;height:262px;overflow:hidden}
.event-card .lbl{position:absolute;bottom:22px;font-size:24px;font-weight:700;color:var(--white);width:100%;text-align:center;white-space:nowrap}

/* offer */
.offer-circle{width:122px;height:122px;border-radius:50%;background:var(--rose);border:2px dashed #f1e4df;outline:3px solid var(--rose);display:flex;align-items:center;justify-content:center}
.offer-lbl{font-size:16px;line-height:20px;color:#333}

/* banner */
.banner{left:0;top:2536px;width:1200px;height:494px;background:linear-gradient(160deg,#3a2e29,#4c3c33 50%,#33302c)}
.banner h3{position:absolute;left:0;width:1200px;top:72px;text-align:center;color:var(--white);font-size:51px;font-weight:600;line-height:66px}
.banner p{position:absolute;left:0;width:1200px;top:216px;text-align:center;color:var(--white);font-size:14.5px;line-height:22px}
.balloons{left:930px;top:2862px;width:270px;height:610px;border-radius:135px 135px 20px 20px;background:linear-gradient(180deg,#d8564a 0%,#e7b84a 22%,#7a8fd0 40%,rgba(220,220,220,.55) 62%,rgba(255,255,255,0) 100%)}

/* work */
.step{width:108px;height:108px;border-radius:50%;border:2px solid var(--ink);display:flex;align-items:center;justify-content:center;background:var(--white)}
.step-lbl{width:220px;text-align:center;font-size:18px;line-height:26px;color:#222}

/* testimonial */
.testimonial{left:0;top:3478px;width:1200px;height:498px;background:linear-gradient(150deg,#6b5a4c,#8a7462 50%,#5a4a40)}
.arrow-c{width:46px;height:46px;border-radius:50%;background:rgba(255,255,255,.35);display:flex;align-items:center;justify-content:center}

/* contact */
.contact-dark{left:0;top:4546px;width:1200px;height:587px;background:var(--dark)}
.contact-card{left:86px;top:3976px;width:1044px;height:736px;background:var(--white)}
.c-field{position:absolute;font-size:16px;color:#9a9a9a;display:flex;align-items:center;gap:10px}
.c-line{position:absolute;height:1px;background:var(--line)}

/* footer */
.footer-brand{left:0;width:1200px;top:4786px;display:flex;justify-content:center;align-items:center;gap:16px;color:var(--white);font-weight:600;font-size:44px;letter-spacing:2px}
.footer-brand .dot{width:86px;height:86px;border-radius:50%;background:var(--white)}
.f-contact{top:4968px;display:flex;gap:16px;color:var(--white);font-size:14px;line-height:18px;white-space:nowrap}
.f-ico{width:34px;height:34px;border:2px solid var(--white);display:flex;align-items:center;justify-content:center;flex:none}
.social{top:4976px;width:32px;height:32px;border:2px solid var(--white)}
.f-rule{left:106px;top:5050px;width:1020px;height:1px;background:#777}
.f-copy{left:106px;top:5068px;color:var(--white);font-size:14px}
.f-links{right:74px;top:5070px;color:var(--white);font-size:14px}
</style>
</head>
<body>

<!-- top bar -->
<div class="abs topbar">
  <div class="item" style="left:716px">
    <svg width="18" height="18" viewBox="0 0 24 24" fill="#fff"><path d="M6.6 10.8a15 15 0 0 0 6.6 6.6l2.2-2.2c.3-.3.7-.4 1-.2 1.1.4 2.3.6 3.6.6.6 0 1 .4 1 1V20c0 .6-.4 1-1 1A17 17 0 0 1 3 4c0-.6.4-1 1-1h3.5c.6 0 1 .4 1 1 0 1.3.2 2.5.6 3.6.1.3 0 .7-.2 1z"/></svg>
    555-014-2290
  </div>
  <div class="sep"></div>
  <div class="item" style="left:894px">
    <svg width="20" height="16" viewBox="0 0 24 18" fill="#fff"><path d="M0 0h24v18H0z"/><path d="M1 1l11 8 11-8" stroke="#1b1b1b" stroke-width="2" fill="none"/></svg>
    hello@ivylantern.example
  </div>
</div>

<!-- header -->
<div class="abs header"></div>
<div class="abs logo-bump"></div>
<div class="abs brand"><span class="dot"></span>THE IVY LANTERN HALL</div>
<nav class="abs nav"><span>HOME</span><span>ABOUT US</span><span>EVENTS</span><span>PAGES</span><span>BLOG</span><span>CONTACT US</span></nav>

<!-- hero -->
<section class="abs hero" role="img" aria-label="Restored bank building event room with brick walls, sofa and rug">
  <h1>HELPING YOU<br>CELEBRATE</h1>
  <div class="cta">GET STARTED</div>
</section>
<div class="abs hero-arch" role="img" aria-label="Photo of children in party hats around a birthday cake"></div>

<!-- booking -->
<section class="abs booking">
  <div class="abs center" style="left:0;width:1104px;top:64px">
    <div class="h2" style="font-size:33px;font-weight:500">BOOK YOUR EVENT</div>
  </div>
  <svg class="abs" style="left:522px;top:116px" width="62" height="8"><circle cx="3" cy="4" r="2.5" fill="#555"/><line x1="6" y1="4" x2="56" y2="4" stroke="#555" stroke-dasharray="3 2"/><circle cx="59" cy="4" r="2.5" fill="#555"/></svg>
  <div class="field" style="left:36px;width:254px">Your Name</div>
  <div class="field" style="left:306px;width:254px;top:164px">Select Event
    <svg width="10" height="14" viewBox="0 0 10 14"><path d="M5 0l4 5H1zM5 14l4-5H1z" fill="#333"/></svg></div>
  <div class="field" style="left:572px;width:254px;top:164px">Select Date
    <svg width="14" height="14" viewBox="0 0 14 14" fill="none" stroke="#555"><rect x="1" y="2" width="12" height="11"/><line x1="1" y1="5" x2="13" y2="5"/></svg></div>
  <div class="abs btn-dark" style="left:846px;top:162px;width:212px;height:72px">BOOK NOW</div>
</section>

<!-- events -->
<div class="abs center" style="left:0;width:1200px;top:1330px;display:flex;justify-content:center;align-items:center;gap:10px">
  <span style="width:58px;height:58px;border-radius:50%;background:var(--ink);display:block"></span>
  <span class="h2" style="font-size:38px">OUR <b>EVENTS</b></span>
</div>
<svg class="abs" style="left:1086px;top:1422px" width="100" height="24" viewBox="0 0 100 24" fill="none" stroke-width="2"><path d="M36 12H4M12 4l-8 8 8 8" stroke="#999"/><path d="M62 12h32M86 4l8 8-8 8" stroke="#111"/></svg>

<div class="abs event-card" style="left:0;width:312px;background:linear-gradient(160deg,#e3dfdc,#c9b8b2 60%,#7a6259)" role="img" aria-label="Baby shower photo with balloons">
  <div class="lbl" style="text-align:left;padding-left:48px">BABY SHOWERS</div></div>
<div class="abs event-card" style="left:320px;width:326px;background:linear-gradient(160deg,#7a2e26,#9a5a48 50%,#4a3128)" role="img" aria-label="Children celebrating a birthday party">
  <div class="abs" style="left:84px;top:88px;width:158px;height:66px;border:2px solid #fff;color:#fff;display:flex;align-items:center;justify-content:center;font-size:17px">BOOK NOW</div>
  <div class="lbl">BITRHDAYS</div></div>
<div class="abs event-card" style="left:660px;width:326px;background:linear-gradient(160deg,#2a1d5e,#5a3aa8 45%,#1a1530)" role="img" aria-label="Crowd at a mixer under stage lights">
  <div class="lbl">MIXERS</div></div>
<div class="abs event-card" style="left:996px;width:204px;background:linear-gradient(160deg,#d8d2cc,#b9aaa3 60%,#6e5c54)" role="img" aria-label="Engagement party guests">
  <div class="abs" style="left:88px;top:110px;width:38px;height:38px;border-radius:50%;background:rgba(255,255,255,.6);display:flex;align-items:center;justify-content:center"><svg width="10" height="14"><path d="M2 2l6 5-6 5" stroke="#333" stroke-width="2" fill="none"/></svg></div>
  <div class="lbl" style="text-align:left;padding-left:62px">ENGAEMEN</div></div>

<!-- offer -->
<div class="abs center" style="left:0;width:1200px;top:1850px"><div class="h2" style="font-size:38px">WHAT WE&nbsp; <b>OFFER</b></div></div>
<svg class="abs" style="left:558px;top:1910px" width="84" height="8"><circle cx="3" cy="4" r="2.5" fill="#555"/><line x1="6" y1="4" x2="78" y2="4" stroke="#555" stroke-dasharray="3 2"/><circle cx="81" cy="4" r="2.5" fill="#555"/></svg>

<div class="abs" style="left:436px;top:2100px;width:328px;height:322px;border-radius:164px 164px 0 0;background:linear-gradient(180deg,#8a4a36,#6a3526 60%,#4e2a20)" role="img" aria-label="Brick facade of the historic bank building with arched doorway"></div>

<div class="abs offer-circle" style="left:425px;top:1966px"><svg width="60" height="60" viewBox="0 0 60 60" fill="none" stroke="#fff" stroke-width="2"><path d="M12 30h36l-4 8H16z"/><path d="M20 30v-8h20v8M26 22v-6h8v6M30 16v-4"/><line x1="30" y1="38" x2="30" y2="50"/><line x1="22" y1="50" x2="38" y2="50"/></svg></div>
<div class="abs offer-lbl" style="left:290px;top:2008px;width:126px;text-align:right">Catering and<br>Décor</div>

<div class="abs offer-circle" style="left:629px;top:1966px"><svg width="60" height="60" viewBox="0 0 60 60" fill="none" stroke="#fff" stroke-width="2"><rect x="10" y="20" width="40" height="28" rx="3"/><path d="M22 20l4-6h8l4 6"/><circle cx="30" cy="34" r="8"/></svg></div>
<div class="abs offer-lbl" style="left:768px;top:2006px">Photos &amp;<br>Videos</div>

<div class="abs offer-circle" style="left:307px;top:2092px"><svg width="60" height="60" viewBox="0 0 60 60" fill="none" stroke="#fff" stroke-width="2"><path d="M10 26l20-14 20 14v24H10z"/><path d="M10 26l20 14 20-14"/><rect x="18" y="18" width="24" height="16"/></svg></div>
<div class="abs offer-lbl" style="left:196px;top:2140px;width:104px;text-align:right">Invitation<br>Cards</div>

<div class="abs offer-circle" style="left:771px;top:2092px"><svg width="60" height="60" viewBox="0 0 60 60" fill="none" stroke="#fff" stroke-width="2"><path d="M12 50l10-28 18 18z"/><path d="M34 20l6-8M40 26l10-2M30 14l2-6M44 16l4-4"/></svg></div>
<div class="abs offer-lbl" style="left:906px;top:2134px">Entertainment</div>

<div class="abs offer-circle" style="left:292px;top:2260px"><svg width="60" height="60" viewBox="0 0 60 60" fill="none" stroke="#fff" stroke-width="2"><path d="M30 52V24"/><circle cx="24" cy="18" r="6"/><circle cx="38" cy="24" r="6"/><path d="M30 40c-6 0-12-4-12-10M30 34c6 0 10-2 12-6"/></svg></div>
<div class="abs offer-lbl" style="left:190px;top:2310px;width:92px;text-align:right">Floral<br>Services</div>

<div class="abs offer-circle" style="left:797px;top:2260px"><svg width="60" height="60" viewBox="0 0 60 60" fill="none" stroke="#fff" stroke-width="2"><path d="M30 50s-14-14-14-24a14 14 0 0 1 28 0c0 10-14 24-14 24z"/><circle cx="30" cy="26" r="5"/><line x1="14" y1="52" x2="46" y2="52"/></svg></div>
<div class="abs offer-lbl" style="left:940px;top:2310px;text-align:center">Venue<br>Selection</div>

<!-- banner -->
<section class="abs banner" role="img" aria-label="Event room with sofa under exposed brick walls">
  <h3>Planning and Organizing<br>Unforgettable Events</h3>
  <p>Lorem ipsum dolor sit amet conse ctetur adipiscing eli tsed do eiusod tempor<br>incididunt ut labore et dolore magna ut labore et dolore magna</p>
  <div class="abs" style="left:486px;top:286px;width:228px;height:96px;border:2px solid #fff;padding:10px">
    <div style="background:#fff;height:72px;display:flex;align-items:center;justify-content:center;font-size:16px;color:#222">BOOK NOW</div>
  </div>
</section>
<div class="abs balloons" role="img" aria-label="Bunch of colourful party balloons on long strings"></div>

<!-- how we work -->
<div class="abs center" style="left:0;width:1200px;top:3110px"><div class="h2" style="font-size:38px">HOW WE&nbsp; <b>WORK</b></div></div>
<svg class="abs" style="left:546px;top:3168px" width="84" height="8"><circle cx="3" cy="4" r="2.5" fill="#555"/><line x1="6" y1="4" x2="78" y2="4" stroke="#555" stroke-dasharray="3 2"/><circle cx="81" cy="4" r="2.5" fill="#555"/></svg>

<svg class="abs" style="left:340px;top:3240px" width="560" height="30" fill="none" stroke="#ccc" stroke-width="1.5"><path d="M16 24q40-26 80 0M226 24q40-26 80 0M434 24q40-26 80 0"/></svg>
<div class="abs step" style="left:238px;top:3216px"><svg width="44" height="44" viewBox="0 0 44 44" fill="none" stroke="#222" stroke-width="2"><path d="M22 36s-10-10-10-18a10 10 0 0 1 20 0c0 8-10 18-10 18z"/><circle cx="22" cy="18" r="4"/><ellipse cx="22" cy="38" rx="12" ry="3"/></svg></div>
<div class="abs step" style="left:454px;top:3216px"><svg width="48" height="44" viewBox="0 0 48 44" fill="none" stroke="#222" stroke-width="2"><rect x="6" y="20" width="24" height="16"/><path d="M4 20h28M12 20v-6h12v6"/><circle cx="38" cy="16" r="6"/><path d="M38 22v14"/></svg></div>
<div class="abs step" style="left:664px;top:3216px"><svg width="48" height="44" viewBox="0 0 48 44" fill="none" stroke="#222" stroke-width="2"><circle cx="14" cy="10" r="4"/><path d="M14 14v16M8 20h12M10 40l4-10 4 10"/><rect x="24" y="18" width="20" height="4"/><path d="M26 22v16M42 22v16M24 10l4 4 4-4 4 4 4-4 4 4"/></svg></div>
<div class="abs step" style="left:866px;top:3216px"><svg width="48" height="44" viewBox="0 0 48 44" fill="none" stroke="#222" stroke-width="2"><path d="M8 40l8-22 14 14z"/><path d="M26 14l6-8M32 20l10-2M22 8l2-6M36 10l4-4M40 28l4 2"/></svg></div>
<div class="abs step-lbl" style="left:182px;top:3346px">FIND THE PERFECT<br>VENUE</div>
<div class="abs step-lbl" style="left:398px;top:3346px">CONNECT WITH<br>THE BEST VENDOR</div>
<div class="abs step-lbl" style="left:606px;top:3346px">LET US HELP YOU<br>WITH THE EVENT</div>
<div class="abs step-lbl" style="left:810px;top:3346px">ENJOY YOUR<br>PERFECT EVENT</div>

<!-- testimonials -->
<section class="abs testimonial" role="img" aria-label="Children celebrating at a party, softly darkened">
  <div class="abs" style="left:108px;top:18px;font-family:'Oswald',sans-serif;font-size:220px;line-height:220px;color:#fff">“</div>
  <div class="abs" style="left:328px;top:100px;color:#fff;font-size:45px">WHAT OUR <b style="font-weight:600">CLIENTS SAY</b></div>
  <svg class="abs" style="left:546px;top:164px" width="84" height="8"><circle cx="3" cy="4" r="2.5" fill="#fff"/><line x1="6" y1="4" x2="78" y2="4" stroke="#fff" stroke-dasharray="3 2"/><circle cx="81" cy="4" r="2.5" fill="#fff"/></svg>
  <div class="abs arrow-c" style="left:66px;top:212px"><svg width="10" height="14"><path d="M8 2L2 7l6 5" stroke="#fff" stroke-width="2" fill="none"/></svg></div>
  <div class="abs arrow-c" style="left:1106px;top:212px"><svg width="10" height="14"><path d="M2 2l6 5-6 5" stroke="#fff" stroke-width="2" fill="none"/></svg></div>
  <p class="abs center" style="left:0;width:1200px;top:222px;color:#fff;font-size:14.5px;line-height:21px">Lorem ipsum, or lipsum as it is sometimes known, is dummy text used in laying out<br>print, graphic or web designs. The passage is attributed<br>unknown typesetter in the 15th century</p>
  <div class="abs" style="left:498px;top:320px;width:86px;height:86px;border-radius:50%;background:linear-gradient(160deg,#e9e4df,#b8b0a8);border:3px solid #fff" role="img" aria-label="Client portrait"></div>
  <div class="abs" style="left:604px;top:334px;color:#fff">
    <div style="font-size:14px;font-weight:600">Maren Holloway</div>
    <div style="font-size:9px">CEO, Fernwick Inc</div>
    <div style="color:#ffcc00;font-size:13px;letter-spacing:1px">★★★★★</div>
  </div>
</section>

<!-- contact -->
<div class="abs contact-dark"></div>
<div class="abs contact-card"></div>
<div class="abs" style="left:180px;top:4116px;font-size:44px">GET IN <b style="font-weight:600">TOUCH</b></div>
<svg class="abs" style="left:298px;top:4184px" width="84" height="8"><circle cx="3" cy="4" r="2.5" fill="#222"/><line x1="6" y1="4" x2="78" y2="4" stroke="#222" stroke-dasharray="3 2"/><circle cx="81" cy="4" r="2.5" fill="#222"/></svg>

<div class="c-field" style="left:156px;top:4284px"><svg width="12" height="14" viewBox="0 0 12 14" fill="#333"><circle cx="6" cy="4" r="3.5"/><path d="M0 14c0-4 3-6 6-6s6 2 6 6z"/></svg>Your Name</div>
<div class="c-field" style="left:402px;top:4284px"><svg width="16" height="12" viewBox="0 0 16 12" fill="#333"><rect width="16" height="12"/><path d="M1 1l7 5 7-5" stroke="#fff" fill="none"/></svg>E-Mail</div>
<div class="c-line" style="left:150px;top:4318px;width:468px"></div>
<div class="c-field" style="left:156px;top:4368px"><svg width="10" height="16" viewBox="0 0 10 16" fill="none" stroke="#333" stroke-width="2"><rect x="1" y="1" width="8" height="14" rx="1"/></svg>Phone Number</div>
<div class="c-field" style="left:402px;top:4368px"><svg width="12" height="16" viewBox="0 0 12 16" fill="#333"><path d="M6 16S0 9 0 6a6 6 0 0 1 12 0c0 3-6 10-6 10z"/><circle cx="6" cy="6" r="2" fill="#fff"/></svg>Address</div>
<div class="c-line" style="left:150px;top:4402px;width:468px"></div>
<div class="c-field" style="left:150px;top:4448px"><svg width="14" height="14" viewBox="0 0 14 14" fill="#333"><circle cx="7" cy="7" r="7"/></svg>Message</div>
<div class="c-line" style="left:150px;top:4482px;width:468px"></div>
<div class="abs btn-dark" style="left:262px;top:4550px;width:150px;height:62px;font-size:15px">SUBMIT NOW</div>
<div class="abs" style="left:658px;top:4138px;width:422px;height:478px;border-radius:211px 211px 0 0;background:linear-gradient(180deg,#9a553c,#7a3f2c 60%,#5e3024)" role="img" aria-label="Corner of the brick bank building with street clock"></div>

<!-- footer -->
<div class="abs footer-brand"><span class="dot"></span>THE IVY LANTERN HALL</div>

<div class="abs f-contact" style="left:104px"><div class="f-ico"><svg width="16" height="16" viewBox="0 0 24 24" fill="#fff"><path d="M6.6 10.8a15 15 0 0 0 6.6 6.6l2.2-2.2c.3-.3.7-.4 1-.2 1.1.4 2.3.6 3.6.6.6 0 1 .4 1 1V20c0 .6-.4 1-1 1A17 17 0 0 1 3 4c0-.6.4-1 1-1h3.5c.6 0 1 .4 1 1 0 1.3.2 2.5.6 3.6.1.3 0 .7-.2 1z"/></svg></div><div>PHONE NUMBER<br>+1 555 014 7730</div></div>
<div class="abs f-contact" style="left:322px"><div class="f-ico"><svg width="16" height="12" viewBox="0 0 16 12" fill="#fff"><rect width="16" height="12"/><path d="M1 1l7 5 7-5" stroke="#222" fill="none"/></svg></div><div>EMAIL<br>info@ivylantern.example</div></div>
<div class="abs f-contact" style="left:570px"><div class="f-ico"><svg width="12" height="16" viewBox="0 0 12 16" fill="#fff"><path d="M6 16S0 9 0 6a6 6 0 0 1 12 0c0 3-6 10-6 10z"/><circle cx="6" cy="6" r="2" fill="#222"/></svg></div><div>Address Line here<br>Pin: 123456</div></div>
<div class="abs social" style="left:1006px"></div>
<div class="abs social" style="left:1050px"></div>
<div class="abs social" style="left:1094px"></div>

<div class="abs f-rule"></div>
<div class="abs f-copy">Copyright @ 2023 All rights reserved</div>
<div class="abs f-links">HOME &nbsp;|&nbsp; ABOUT US &nbsp;|&nbsp; EVENTS &nbsp;|&nbsp; SERVICES &nbsp;|&nbsp; CONTACT US</div>

</body>
</html>
```